Website design for legal tech start up in Switzerland (B2B)

We are for a legal tech start up in Switzerland called MIVA. We have been running since August 2016. This will be our first live website.

We need a website designed and business card design for our start-up in Switzerland. We also need the Web design to be converted into HTML and CSS files.

Function of website:
• To inform potential customers of our services
• Form a key part of our digital marketing and sales footprint.
• Branding

Please find attached logo.

Reason: Looking for more idea's not necessarily set on blue and grey colours only.

Target Market(s)

B2B tech powered legal services.

Industry/Entity Type

Legal

Contact Information for Business Card

Lean and slick design.

Coding

Coded - Design and coding required

Number of Pages Required

5+ page

Requirements
Must have
• VERY LEAN AND CLEAN DESIGN!
• We have received many great standard designs, but we are looking for something more out-of-the box: You can get inspiration from these designs: http://www.plimbergallery.net/websites/clean/
• Thanks!!
• Easy content management system
• Well structured coding for additional development
• Responsive webpage for all types of devices
• SEO optimized
• Tabs (Home, services, team, careers, blog, contact us)
• Colour scheme complementary to logo
Nice to have
• Look and Design - Approachable, High-tech, Modern
• Easy to add chat bot capability in future
Should not have
• Too busy/ too much clutter
• Not take to long to load

```html
<!DOCTYPE html>
<html lang="en">
<head>
<meta charset="utf-8">
<title>MIVA — Legal Services</title>
<link rel="stylesheet" href="https://fonts.googleapis.com/css2?family=Montserrat:wght@400;500;600;700&display=swap">
<style>
:root{
  --navy:#1d3d72;
  --navy-dark:#152f5a;
  --navy-deep:#122a52;
  --orange:#f5a623;
  --ink:#2b2b2b;
  --text:#555b66;
  --muted:#8a8f98;
  --line:#d9dde3;
  --light:#f3f4f6;
  --white:#ffffff;
}
*{box-sizing:border-box;margin:0;padding:0}
html,body{width:1200px;height:3303px;overflow:hidden}
body{font-family:"Montserrat",Arial,sans-serif;color:var(--text);background:var(--white);font-size:12px}
.wrap{position:relative;width:1014px;margin:0 auto;height:100%}
section,header,footer,nav{position:relative;width:1200px}

/* top bar */
.topbar{height:31px;background:#f5f5f5;font-size:11px;color:#555}
.topbar .hours{position:absolute;left:0;top:9px;display:flex;align-items:center;gap:7px;white-space:nowrap}
.topbar .social{position:absolute;right:0;top:7px;display:flex;gap:6px}
.topbar .social span{width:16px;height:16px;background:var(--navy);border-radius:2px}

/* header */
.masthead{height:90px}
.brand{position:absolute;left:0;top:14px;font-size:58px;font-weight:700;letter-spacing:3px;color:var(--navy-deep);line-height:1}
.contact-item{position:absolute;top:30px;display:flex;gap:10px;align-items:flex-start;font-size:11px;color:#333;line-height:1.45;font-weight:500;white-space:nowrap}
.contact-item svg{flex:none;margin-top:2px}

/* nav */
.mainnav{height:40px;background:var(--navy)}
.mainnav ul{list-style:none;position:absolute;left:0;top:0;height:40px}
.mainnav li{position:absolute;top:0;height:40px;line-height:40px;color:var(--white);font-size:11px;font-weight:500;white-space:nowrap}
.mainnav li.active{border-bottom:3px solid var(--white)}
.cta-eval{position:absolute;right:0;top:7px;height:26px;width:198px;background:var(--orange);color:var(--white);border-radius:13px;font-size:11px;font-weight:600;display:flex;align-items:center;justify-content:center;gap:6px;white-space:nowrap}

/* hero */
.hero{height:440px;background:linear-gradient(180deg,#e4ebf3 0%,#c9d5e3 55%,#b3c2d4 100%)}
.hero-portrait{position:absolute;left:590px;top:0;width:363px;height:440px;background:linear-gradient(180deg,#c7ccd4 0%,#6f747c 55%,#3e434b 100%)}
.hero h1{position:absolute;left:0;top:95px;font-size:50px;font-weight:500;color:#333;letter-spacing:-.5px;white-space:nowrap}
.hero p{position:absolute;left:0;top:170px;width:480px;font-size:13px;line-height:1.55;color:#333}
.btn{display:inline-flex;align-items:center;justify-content:center;background:var(--navy);color:var(--white);font-weight:600;font-size:13px;white-space:nowrap}
.hero .btn{position:absolute;left:0;top:275px;width:145px;height:55px}

/* section titles */
.section-title{position:absolute;left:0;width:100%;text-align:center;font-size:20px;font-weight:500;color:var(--ink);letter-spacing:.5px}
.section-title::after{content:"";display:block;width:66px;height:3px;background:var(--navy);margin:18px auto 0}

/* offer */
.offer{height:363px}
.offer .section-title{top:56px}
.service{position:absolute;top:150px;width:230px;text-align:center}
.service svg{display:block;margin:0 auto}
.service h3{margin-top:16px;font-size:15px;font-weight:500;color:var(--navy-deep)}
.service p{margin-top:10px;font-size:11.5px;line-height:1.55;color:#444}

/* about */
.about{height:353px;background:linear-gradient(90deg,#2e5386 0%,#5677a3 45%,#3a5c8d 100%);color:var(--white)}
.about .section-title{top:52px;color:var(--white)}
.about .section-title::after{background:var(--white)}
.about .copy{position:absolute;left:92px;top:125px;width:830px;text-align:center;font-size:12px;line-height:1.6}
.about .copy p+p{margin-top:14px}

/* team */
.team{height:533px;background:var(--light)}
.team .section-title{top:56px}
.member{position:absolute;top:147px;width:233px;height:324px;background:var(--white);text-align:center}
.member .photo{height:227px;background:linear-gradient(180deg,#f4f4f4 0%,#cfd2d7 60%,#4a4f58 100%)}
.member h4{margin-top:17px;font-size:15px;font-weight:500;color:var(--navy-deep)}
.member .role{margin-top:4px;font-size:11px;color:#555}
.member .social{margin-top:12px;border-top:1px solid var(--line);padding-top:12px;display:flex;justify-content:center;gap:12px}
.member .social span{width:9px;height:9px;background:var(--navy-deep);border-radius:50%}

/* blog */
.blog{height:590px}
.blog .section-title{top:45px}
.post{position:absolute;top:134px;width:321px}
.post .thumb{position:relative;height:211px;background:linear-gradient(135deg,#9fb1c6 0%,#5b6f88 50%,#2c3a52 100%)}
.post .date{position:absolute;left:7px;bottom:0;height:26px;padding:0 14px;background:var(--navy-deep);color:var(--white);font-size:10px;font-weight:500;line-height:26px;white-space:nowrap}
.post h3{margin-top:18px;font-size:15px;font-weight:600;line-height:1.35;color:var(--navy-deep)}
.post p{margin-top:8px;font-size:11.5px;line-height:1.55;color:#444}
.post .more{display:inline-block;margin-top:12px;font-size:10px;font-weight:600;color:var(--navy-deep);border-bottom:1px solid var(--navy-deep)}

/* consultation */
.consult{height:517px;background:linear-gradient(90deg,#f6f6fb 0%,#e7e9f5 55%,#d4d9e8 100%)}
.consult-art{position:absolute;right:0;top:0;width:430px;height:517px;background:linear-gradient(180deg,rgba(160,170,195,.25),rgba(120,130,160,.35))}
.consult .section-title{top:52px}
.consult .intro{position:absolute;top:127px;width:100%;text-align:center;font-size:12px;color:#333}
.field{position:absolute;background:var(--white);border-bottom:2px solid var(--navy);font-size:11px;color:#888;padding:18px 12px}
.consult .btn{position:absolute;left:433px;top:418px;width:146px;height:46px;font-size:14px}

/* footer */
.site-footer{height:306px;background:var(--navy);color:var(--white)}
.site-footer .brand{top:68px;font-size:44px;color:var(--white)}
.foot-about{position:absolute;left:0;top:126px;width:225px;font-size:11px;line-height:1.5}
.foot-follow{position:absolute;left:0;top:184px;font-size:12px;font-weight:600}
.foot-social{position:absolute;left:0;top:208px;display:flex;gap:14px}
.foot-social span{width:9px;height:9px;background:var(--white);border-radius:50%}
.foot-col{position:absolute;top:52px}
.foot-col h5{font-size:13px;font-weight:600;letter-spacing:.3px;margin-bottom:14px;white-space:nowrap}
.foot-col ul{list-style:none;font-size:11px;line-height:1.4}
.foot-col li{position:relative;padding-left:14px;margin-bottom:8px}
.foot-col li::before{content:"›";position:absolute;left:0;top:-1px;font-weight:700}
.foot-links{display:grid;grid-template-columns:120px 100px}
.contact-list li::before{content:none}
.contact-list li{padding-left:0;display:flex;gap:8px;align-items:center;margin-bottom:18px;white-space:nowrap}
.copyright{height:40px;background:var(--navy-deep);color:var(--white);font-size:11px}
.copyright span{position:absolute;top:13px;white-space:nowrap}
</style>
</head>
<body>

<div class="topbar"><div class="wrap">
  <div class="hours">
    <svg width="12" height="12" viewBox="0 0 12 12"><circle cx="6" cy="6" r="5" fill="none" stroke="#1d3d72" stroke-width="1.4"/><path d="M6 3v3l2 1.5" fill="none" stroke="#1d3d72" stroke-width="1.4"/></svg>
    Mon - Fri 08.00am - 05.00pm
  </div>
  <div class="social"><span></span><span></span><span></span></div>
</div></div>

<header class="masthead"><div class="wrap">
  <div class="brand">MIVA</div>
  <div class="contact-item" style="left:447px">
    <svg width="16" height="22" viewBox="0 0 16 22"><path d="M8 1a7 7 0 0 0-7 7c0 5 7 13 7 13s7-8 7-13a7 7 0 0 0-7-7z" fill="#1d3d72"/><circle cx="8" cy="8" r="2.6" fill="#fff"/></svg>
    <div>1234 Street Address,<br>City, Switzerland</div>
  </div>
  <div class="contact-item" style="left:650px">
    <svg width="26" height="20" viewBox="0 0 26 20"><rect x="1" y="1" width="24" height="18" rx="1" fill="none" stroke="#1d3d72" stroke-width="2"/><path d="M1 2l12 9 12-9" fill="none" stroke="#1d3d72" stroke-width="2"/></svg>
    <div>Email us at<br>admin@domain.com</div>
  </div>
  <div class="contact-item" style="left:870px">
    <svg width="20" height="20" viewBox="0 0 20 20"><path d="M4 1l4 4-2 3c1.5 3 3 4.5 6 6l3-2 4 4-3 3C9 19 1 11 1 4z" fill="#1d3d72"/></svg>
    <div>Call us for help<br>+41 987 -123-0456</div>
  </div>
</div></header>

<nav class="mainnav"><div class="wrap">
  <ul>
    <li class="active" style="left:0">HOME</li>
    <li style="left:99px">SERVICES</li>
    <li style="left:211px">TEAM</li>
    <li style="left:297px">CAREERS</li>
    <li style="left:402px">BLOG</li>
    <li style="left:490px">CONTACT US</li>
  </ul>
  <div class="cta-eval">
    <svg width="10" height="12" viewBox="0 0 10 12"><rect x="1" y="1" width="8" height="10" fill="none" stroke="#fff" stroke-width="1.4"/></svg>
    FREE CASE EVALUATION
  </div>
</div></nav>

<section class="hero">
  <div class="wrap">
    <div class="hero-portrait" role="img" aria-label="Portrait of a smiling lawyer in a grey suit in front of a city skyline"></div>
    <h1>Welcome to MIVA</h1>
    <p>Practical legal guidance for modern businesses. Clear advice, fair fees and fast answers from a team that knows Swiss law. Contracts, disputes and compliance handled by people who listen and respond quickly.</p>
    <a class="btn">CONTACT US</a>
  </div>
</section>

<section class="offer"><div class="wrap">
  <h2 class="section-title">WHAT WE OFFER</h2>
  <div class="service" style="left:0">
    <svg width="36" height="32" viewBox="0 0 36 32"><path d="M18 1L2 9h32z" fill="#1d3d72"/><rect x="5" y="11" width="4" height="14" fill="#1d3d72"/><rect x="13" y="11" width="4" height="14" fill="#1d3d72"/><rect x="21" y="11" width="4" height="14" fill="#1d3d72"/><rect x="29" y="11" width="4" height="14" fill="#1d3d72"/><rect x="2" y="27" width="32" height="4" fill="#1d3d72"/></svg>
    <h3>Labour Law</h3>
    <p>Support for employers on contracts, hiring, dismissals and workplace policy, with simple steps you can act on.</p>
  </div>
  <div class="service" style="left:261px">
    <svg width="34" height="32" viewBox="0 0 34 32"><rect x="6" y="2" width="16" height="8" rx="1" transform="rotate(45 14 6)" fill="#1d3d72"/><rect x="12" y="12" width="18" height="4" transform="rotate(45 12 12)" fill="#1d3d72"/><rect x="2" y="27" width="18" height="4" fill="#1d3d72"/></svg>
    <h3>Criminal Law</h3>
    <p>Discreet defence and clear counsel for firms and their staff facing inquiries, charges or court hearings.</p>
  </div>
  <div class="service" style="left:519px">
    <svg width="34" height="32" viewBox="0 0 34 32"><rect x="12" y="2" width="10" height="6" fill="none" stroke="#1d3d72" stroke-width="2.5"/><rect x="2" y="8" width="30" height="22" rx="2" fill="#1d3d72"/></svg>
    <h3>Corporate law</h3>
    <p>Company formation, shareholder deals, funding rounds and governance set up cleanly from the first day.</p>
  </div>
  <div class="service" style="left:778px">
    <svg width="34" height="32" viewBox="0 0 34 32"><path d="M17 30L4 17a8 8 0 0 1 13-10 8 8 0 0 1 13 10z" fill="none" stroke="#1d3d72" stroke-width="2.5"/><path d="M6 16h7l2-4 3 8 2-4h8" fill="none" stroke="#1d3d72" stroke-width="2"/></svg>
    <h3>Health Law</h3>
    <p>Guidance for clinics and health startups on licences, patient data, liability and approvals.</p>
  </div>
</div></section>

<section class="about" role="img" aria-label="Blurred group of business people behind a blue overlay"><div class="wrap">
  <h2 class="section-title">ABOUT MIVA</h2>
  <div class="copy">
    <p>MIVA is a legal tech firm founded in Switzerland in 2016 to make quality legal help simple for growing businesses. We pair experienced lawyers with smart tools, so routine work moves faster and costs stay predictable. Our clients range from young startups to established companies that want clear answers without long waits or surprise invoices. We explain each step in plain language and keep you informed from the first call to the final signature, whatever the size of the matter.</p>
    <p>We believe good advice should be easy to reach. That is why our team works closely with every client, offers fixed fees where possible and shares documents through a secure online space you can open at any time.</p>
  </div>
</div></section>

<section class="team"><div class="wrap">
  <h2 class="section-title">OUR TEAM</h2>
  <div class="member" style="left:0"><div class="photo" role="img" aria-label="Portrait of a lawyer in a suit"></div><h4>John Doe</h4><div class="role">Labour Lawyer</div><div class="social"><span></span><span></span><span></span><span></span></div></div>
  <div class="member" style="left:260px"><div class="photo" role="img" aria-label="Portrait of a lawyer in a suit"></div><h4>Johnny Doe</h4><div class="role">Labour Lawyer</div><div class="social"><span></span><span></span><span></span><span></span></div></div>
  <div class="member" style="left:520px"><div class="photo" role="img" aria-label="Portrait of a lawyer in a suit"></div><h4>Joe Doe</h4><div class="role">Labour Lawyer</div><div class="social"><span></span><span></span><span></span><span></span></div></div>
  <div class="member" style="left:781px"><div class="photo" role="img" aria-label="Portrait of a lawyer in a suit"></div><h4>Jonathan Doe</h4><div class="role">Labour Lawyer</div><div class="social"><span></span><span></span><span></span><span></span></div></div>
</div></section>

<section class="blog"><div class="wrap">
  <h2 class="section-title">LATEST BLOGS</h2>
  <article class="post" style="left:0">
    <div class="thumb" role="img" aria-label="Young lawyer standing in front of a domed government building"><span class="date">February 16, 2017</span></div>
    <h3>New rules for employment contracts this year</h3>
    <p>A short guide to the changes employers should check before signing new staff. What shifts, who is affected and the dates that matter most.</p>
    <a class="more">READ MORE</a>
  </article>
  <article class="post" style="left:347px">
    <div class="thumb" role="img" aria-label="Businessman on a phone walking through a city street"><span class="date">February 15, 2017</span></div>
    <h3>How to protect your startup from early disputes</h3>
    <p>Simple habits for founders that prevent costly arguments later. Agreements, roles and ownership written down before growth begins.</p>
    <a class="more">READ MORE</a>
  </article>
  <article class="post" style="left:693px">
    <div class="thumb" role="img" aria-label="Lawyer writing at a desk beside a statue of justice"><span class="date">February 14, 2017</span></div>
    <h3>Data privacy basics every small firm should know</h3>
    <p>What personal data you may keep, how long to store it and the steps to take when a customer asks to see it.</p>
    <a class="more">READ MORE</a>
  </article>
</div></section>

<section class="consult">
  <div class="consult-art" role="img" aria-label="Faded scales of justice on a soft background"></div>
  <div class="wrap">
    <h2 class="section-title">REQUEST A FREE CONSULTATION</h2>
    <p class="intro">Fill out the form below to recieve a free and confidential intial consultation.</p>
    <div class="field" style="left:0;top:178px;width:233px;height:51px">Full Name*</div>
    <div class="field" style="left:260px;top:178px;width:233px;height:51px">Email Address*</div>
    <div class="field" style="left:520px;top:178px;width:233px;height:51px">Phone Number</div>
    <div class="field" style="left:781px;top:178px;width:233px;height:51px">Subject*</div>
    <div class="field" style="left:0;top:257px;width:1014px;height:128px">Full Case Description</div>
    <a class="btn">SUBMIT</a>
  </div>
</section>

<footer class="site-footer"><div class="wrap">
  <div class="brand">MIVA</div>
  <p class="foot-about">Clear legal help for growing companies across Switzerland, from first idea to final deal.</p>
  <div class="foot-follow">FIND US ON</div>
  <div class="foot-social"><span></span><span></span><span></span><span></span></div>
  <div class="foot-col" style="left:259px">
    <h5>IMPORTANT PAGES</h5>
    <ul class="foot-links"><li>Home</li><li>Careers</li><li>Services</li><li>Blog</li><li>Team</li><li>Contact Us</li><li>Privacy Policy</li><li>Terms</li></ul>
  </div>
  <div class="foot-col" style="left:519px;width:230px">
    <h5>LATEST BLOG POSTS</h5>
    <ul><li>New rules for employment contracts this year<br>February 16, 2017</li><li>How to protect your startup from early disputes<br>February 15, 2017</li><li>Data privacy basics every small firm should know<br>February 14, 2017</li></ul>
  </div>
  <div class="foot-col contact-list" style="left:781px">
    <h5>CONTACT INFORMATION</h5>
    <ul>
      <li><svg width="10" height="13" viewBox="0 0 16 22"><path d="M8 1a7 7 0 0 0-7 7c0 5 7 13 7 13s7-8 7-13a7 7 0 0 0-7-7z" fill="#fff"/></svg>1234 Street Address, City, Switzerland</li>
      <li><svg width="12" height="9" viewBox="0 0 26 20"><rect x="1" y="1" width="24" height="18" fill="none" stroke="#fff" stroke-width="2.5"/><path d="M1 2l12 9 12-9" fill="none" stroke="#fff" stroke-width="2.5"/></svg>admin@domain.com</li>
      <li><svg width="11" height="11" viewBox="0 0 20 20"><path d="M4 1l4 4-2 3c1.5 3 3 4.5 6 6l3-2 4 4-3 3C9 19 1 11 1 4z" fill="#fff"/></svg>+41 987 -123-0456</li>
    </ul>
  </div>
</div></footer>

<div class="copyright" style="position:relative;width:1200px"><div class="wrap">
  <span style="left:0">Copyright 2017 MIVA | All rights reserved.</span>
</div></div>

</body>
</html>
```